Verlane Area Planning Council Business Cards

We're looking for a business card design, simple as that. We're a local government agency that mainly performs building code enforcement, transportation planning, floodplain management, and GIS for Tobinet Parish in Louisiana, and other surround parishes. So you're not having to Google anything, GIS is, at it's core, mapping. Building Code Enforcement is just that, nothing more. Floodplain Management is to make sure the public is within what the government

Contact Information for Business Card

Our Address is

417 Merriwell Avenue
Pellham Ridge 70000

Our phone is 5550192734
Our fax is 5550192739
Our website is www.vlpk.example
My email is dana@vlpk.example

Font styles to use
Serif
Sans Serif

Colors

Designer to choose colors to be used in the design.

Requirements
Must have
• I'm attaching our logo(several versions) that must be incorporated. The design should fit well with our existing logo. I can send photoshop files for our logo if needed. If possible, I'd like to be able to add names/info to each card for all of our employees once this is done.
Nice to have
• The Louisiana state emblem is a bonus, and isn't specifically required.

```html
<!DOCTYPE html>
<html lang="en">
<head>
<meta charset="utf-8">
<title>Verlane Council – Business Card</title>
<link rel="stylesheet" href="https://fonts.googleapis.com/css2?family=Lato:wght@300;400;700&family=Montserrat:wght@700&display=swap">
<style>
  :root {
    --page-bg: #2a2a2b;
    --card-bg: #1f2022;
    --card-back-bg: #1c1d1f;
    --pattern-tone: #252628;
    --text-main: #ffffff;
    --text-soft: #d8d8d8;
    --rule: #7a7a7a;
    --icon-blue: #1f5fd6;
    --icon-orange: #f39a1e;
    --icon-yellow: #d7e21a;
    --icon-green: #3aaa35;
  }
  * { box-sizing: border-box; margin: 0; padding: 0; }
  html, body { width: 1200px; height: 1108px; overflow: hidden; }
  body {
    background: var(--page-bg);
    font-family: "Lato", sans-serif;
    color: var(--text-main);
    position: relative;
  }
  .card {
    position: absolute;
    top: 234px;
    width: 400px;
    height: 640px;
    border-radius: 28px;
    box-shadow: 0 18px 40px rgba(0,0,0,.45);
    overflow: hidden;
  }
  .card--front { left: 150px; background: var(--card-bg); }
  .card--back  { left: 650px; background: var(--card-back-bg); }

  /* front */
  .brand {
    position: absolute; top: 140px; left: 0; right: 0;
    display: flex; flex-direction: column; align-items: center;
  }
  .brand__row { display: flex; align-items: center; gap: 12px; }
  .brand__square { width: 36px; height: 36px; background: var(--icon-green); }
  .brand__name {
    font-family: "Montserrat", sans-serif; font-weight: 700;
    font-size: 46px; letter-spacing: 1px; line-height: 1; color: var(--text-main);
  }
  .brand__tagline {
    margin-top: 10px; font-weight: 300; font-size: 12px;
    color: var(--text-soft); letter-spacing: 2px; text-transform: uppercase;
  }
  .person { position: absolute; top: 318px; left: 0; right: 0; text-align: center; }
  .person__name { font-size: 25px; font-weight: 400; letter-spacing: .5px; text-transform: uppercase; }
  .person__title { font-size: 18px; color: var(--text-soft); margin-top: 2px; }

  .contact-icons {
    position: absolute; top: 398px; left: 40px; right: 40px;
    display: flex; align-items: center; gap: 8px;
  }
  .contact-icons__rule { flex: 1; height: 1px; background: var(--rule); }
  .contact-icons__set { display: flex; gap: 5px; }
  .icon-tile { width: 24px; height: 24px; border-radius: 4px; display: grid; place-items: center; }
  .icon-tile--phone { background: var(--icon-blue); }
  .icon-tile--fax { background: var(--icon-orange); }
  .icon-tile--mail { background: var(--icon-yellow); }
  .icon-tile--web { background: var(--icon-green); }

  .contact-list {
    position: absolute; top: 436px; left: 0; right: 0;
    text-align: center; list-style: none;
    font-size: 19px; line-height: 25px; color: var(--text-soft);
  }
  .address-rule { position: absolute; top: 548px; left: 70px; right: 70px; height: 1px; background: var(--rule); }
  .address {
    position: absolute; top: 558px; left: 0; right: 0;
    text-align: center; font-style: normal;
    font-size: 19px; line-height: 25px; color: var(--text-soft);
  }

  /* back */
  .back-pattern { position: absolute; inset: 0; background: linear-gradient(160deg, var(--pattern-tone), var(--card-back-bg) 70%); }
  .back-name {
    position: absolute; top: 420px; left: 0; right: 0; text-align: center;
    font-family: "Montserrat", sans-serif; font-weight: 700;
    font-size: 30px; letter-spacing: 1px; color: var(--text-main);
  }
</style>
</head>
<body>

<section class="card card--front" aria-label="Card front">
  <div class="brand">
    <div class="brand__row">
      <span class="brand__square" aria-hidden="true"></span>
      <span class="brand__name">VERLANE</span>
    </div>
    <span class="brand__tagline">Tobinet Parish</span>
  </div>

  <div class="person">
    <p class="person__name">Marcus Hale</p>
    <p class="person__title">Managing Director</p>
  </div>

  <div class="contact-icons">
    <span class="contact-icons__rule"></span>
    <div class="contact-icons__set">
      <span class="icon-tile icon-tile--phone">
        <svg width="14" height="14" viewBox="0 0 24 24"><path fill="#fff" d="M6.6 10.8a15 15 0 0 0 6.6 6.6l2.2-2.2c.3-.3.7-.4 1-.2 1.1.4 2.3.6 3.6.6.6 0 1 .4 1 1V20c0 .6-.4 1-1 1A17 17 0 0 1 3 4c0-.6.4-1 1-1h3.5c.6 0 1 .4 1 1 0 1.3.2 2.5.6 3.6.1.3 0 .7-.2 1z"/></svg>
      </span>
      <span class="icon-tile icon-tile--fax">
        <svg width="14" height="14" viewBox="0 0 24 24"><path fill="#fff" d="M7 3h10v5H7zM4 9h16a1 1 0 0 1 1 1v7h-4v4H7v-4H3v-7a1 1 0 0 1 1-1zm5 7v3h6v-3z"/></svg>
      </span>
      <span class="icon-tile icon-tile--mail">
        <svg width="14" height="14" viewBox="0 0 24 24"><path fill="#222" d="M3 5h18v14H3zm2 2v.5l7 5 7-5V7l-7 5z"/></svg>
      </span>
      <span class="icon-tile icon-tile--web">
        <svg width="14" height="14" viewBox="0 0 24 24"><circle cx="12" cy="12" r="8" fill="none" stroke="#fff" stroke-width="2"/><path d="M4 12h16M12 4c3 3 3 13 0 16M12 4c-3 3-3 13 0 16" fill="none" stroke="#fff" stroke-width="1.6"/></svg>
      </span>
    </div>
    <span class="contact-icons__rule"></span>
  </div>

  <ul class="contact-list">
    <li>5550192734</li>
    <li>5550192739</li>
    <li>dana@vlpk.example</li>
    <li>www.vlpk.example</li>
  </ul>

  <span class="address-rule"></span>
  <address class="address">417 Merriwell Avenue<br>Pellham Ridge 70000</address>
</section>

<section class="card card--back" aria-label="Card back">
  <div class="back-pattern" role="img" aria-label="Faint repeated organisation name pattern"></div>
  <p class="back-name">VERLANE</p>
</section>

</body>
</html>
```